KVL cards

Design business cards for renamed business. Korvane Lighting Limited is a leading contract designer of electronic lighting products sepcialising in LED lighting. Need a design that is simple but clear please. Cards for two persons requried.

Target Market(s)

Professional and technical

Industry/Entity Type

Business

Font styles to use
Sans Serif
Other font styles liked:
• tahoma

Colors
ffcf3e

```html
<!DOCTYPE html>
<html lang="en">
<head>
<meta charset="utf-8">
<title>Korvane Lighting Limited – Business Card</title>
<link rel="stylesheet" href="https://fonts.googleapis.com/css2?family=Lato:wght@400;700;900&display=swap">
<style>
  :root {
    --stage: #5b5b5b;
    --card-dark: #0b0b0b;
    --card-dark-soft: #1a1410;
    --brand-yellow: #ffcf3e;
    --ink: #111111;
  }
  * { box-sizing: border-box; margin: 0; padding: 0; }
  html, body {
    width: 1200px; height: 900px; overflow: hidden;
    background: var(--stage);
    font-family: "Lato", Tahoma, sans-serif;
    color: var(--ink);
  }
  .business-card {
    position: absolute; left: 100px; top: 165px;
    width: 1000px; height: 570px;
    border-radius: 30px; overflow: hidden;
    background: var(--card-dark);
  }
  .light-photo {
    position: absolute; left: 0; top: 0; width: 480px; height: 100%;
    background: linear-gradient(135deg, var(--card-dark-soft) 0%, var(--card-dark) 70%);
  }
  .yellow-panel { position: absolute; inset: 0; width: 100%; height: 100%; }
  .card-content { position: absolute; left: 470px; top: 0; right: 30px; height: 100%; }
  .company-name {
    position: absolute; top: 130px; left: 0;
    font-size: 37px; font-weight: 400; white-space: nowrap;
  }
  .company-name strong { font-weight: 900; }
  .person-name {
    position: absolute; top: 240px; left: 0;
    font-size: 40px; font-weight: 400; white-space: nowrap;
  }
  .person-name strong { font-weight: 900; }
  .contact-list {
    position: absolute; top: 320px; left: 0;
    list-style: none; font-size: 26px; line-height: 37px; white-space: nowrap;
  }
  .contact-list li { display: flex; align-items: flex-start; }
  .contact-icon { width: 19px; height: 19px; margin: 9px 15px 0 0; flex: none; }
</style>
</head>
<body>
  <article class="business-card">
    <div class="light-photo" role="img" aria-label="Photograph of blurred coloured LED lights glowing against a black background"></div>
    <svg class="yellow-panel" viewBox="0 0 1000 570" preserveAspectRatio="none" aria-hidden="true">
      <path d="M455 0 Q405 285 455 570 L1000 570 L1000 0 Z" fill="var(--brand-yellow)"/>
    </svg>
    <div class="card-content">
      <h1 class="company-name"><strong>Korvane</strong> Lighting Limited</h1>
      <h2 class="person-name">Ellis <strong>Marren</strong></h2>
      <ul class="contact-list">
        <li>
          <svg class="contact-icon" viewBox="0 0 20 20" aria-hidden="true"><path d="M2 6 Q10 0 18 6 L15 9 L13 7 L7 7 L5 9 Z M4 10 L16 10 L18 18 L2 18 Z" fill="var(--ink)"/></svg>
          555-301-4827
        </li>
        <li>
          <svg class="contact-icon" viewBox="0 0 20 20" aria-hidden="true"><rect x="1" y="4" width="18" height="13" fill="var(--ink)"/><path d="M1 4 L10 11 L19 4" fill="none" stroke="var(--brand-yellow)" stroke-width="1.6"/></svg>
          korvanelight.com
        </li>
        <li>
          <svg class="contact-icon" viewBox="0 0 20 20" aria-hidden="true"><g fill="none" stroke="var(--ink)" stroke-width="2.4" stroke-linecap="round"><path d="M8 12 L12 8"/><path d="M9 6 L11 4 A3.5 3.5 0 0 1 16 9 L14 11"/><path d="M11 14 L9 16 A3.5 3.5 0 0 1 4 11 L6 9"/></g></svg>
          ellis@korvanelight.com
        </li>
        <li>
          <svg class="contact-icon" viewBox="0 0 20 20" aria-hidden="true"><path d="M10 1 L20 10 L17 10 L17 19 L12 19 L12 13 L8 13 L8 19 L3 19 L3 10 L0 10 Z" fill="var(--ink)"/></svg>
          <span>214 Bramley Avenue,<br>Unit 7, Calder Park, NY 14022</span>
        </li>
      </ul>
    </div>
  </article>
</body>
</html>
```